GreenHarborPeak - Double Sided Business Card

We are looking for design options or our business cards. We are a Business Solutions and HR solutions Provider - the theme is business, for this card.

Our brand colours are represented within our logo.

Details needed to be put on the front of the business card are:

Employees name: [Sample Name]
Role: [Sample Role]

Address: Suite 4 - Level 3/48 Lindqvist Avenue Kellyville Ridge NSW 2763
M: 0000 000 000
P: 1300 482 917
F: 1300 482 935
E: sample@greenharborpeak.com.au
www.greenharborpeak.com.au

Reason: Hello, could we please increase our deadline by 5 days. Thanking you, Tamsin

Target Market(s)

Business Owners, also Candidates looking for Employment

Industry/Entity Type

Business

Contact Information for Business Card

Role: [Sample Role]

M: 0000 000 000
P: 1300 482 917
F: 1300 482 935

Font styles to use
Sans Serif

Colors
3276b5
3176b5
0455a3
85abd2
cfdeed
ffffff
000000
1b1b1b
757575

Requirements
Must have
• Details needed to be put on the front of the business card are:
• Employees name: [Sample Name]
• Role: [Sample Role]
• Address: Suite 4 - Level 3/48 Lindqvist Avenue Kellyville Ridge NSW 2763
• M: 0000 000 000
• P: 1300 482 917
• F: 1300 482 935
• E: sample@greenharborpeak.com.au
• www.greenharborpeak.com.au
Nice to have
• Simplicity, clean and professional.

```html
<!DOCTYPE html>
<html lang="en">
<head>
<meta charset="utf-8">
<title>GreenHarborPeak – Business Card</title>
<link rel="stylesheet" href="https://fonts.googleapis.com/css2?family=Open+Sans:wght@400;600;700;800&display=swap">
<style>
  :root {
    --stage: #2b2b2e;
    --brand-blue: #0455a3;
    --mid-blue: #3176b5;
    --light-blue: #85abd2;
    --navy: #0b2447;
    --navy-deep: #071a36;
    --ink: #1b1b1b;
    --grey: #757575;
    --white: #ffffff;
  }
  * { box-sizing: border-box; margin: 0; padding: 0; }
  html, body {
    width: 1200px; height: 925px; overflow: hidden;
    background: var(--stage);
    font-family: "Open Sans", Arial, sans-serif;
  }
  .sheet {
    position: relative; width: 1200px; height: 925px;
    display: flex; align-items: center; justify-content: center; gap: 30px;
  }
  .card {
    position: relative; width: 555px; height: 317px; overflow: hidden;
    box-shadow: 0 10px 30px rgba(0,0,0,.45);
  }

  /* Back side */
  .card--back {
    background: linear-gradient(135deg, var(--navy-deep) 0%, var(--navy) 40%, var(--brand-blue) 100%);
    color: var(--white);
  }
  .back-brand {
    position: absolute; left: 0; right: 0; top: 92px;
    display: flex; flex-direction: column; align-items: center;
  }
  .brand-lockup { display: flex; align-items: center; gap: 10px; white-space: nowrap; }
  .brand-mark { width: 24px; height: 24px; flex: none; }
  .back-brand .brand-mark { background: var(--white); }
  .back-brand .brand-name { font-size: 26px; font-weight: 700; color: var(--white); letter-spacing: .5px; }
  .back-brand .tagline { margin-top: 8px; font-size: 9px; font-weight: 600; color: var(--white); white-space: nowrap; }
  .back-divider {
    position: absolute; left: 150px; right: 60px; top: 222px;
    height: 1px; background: var(--light-blue); opacity: .6;
  }
  .back-web {
    position: absolute; right: 62px; top: 232px;
    font-size: 13px; letter-spacing: 2px; color: var(--white);
  }

  /* Front side */
  .card--front { background: var(--white); color: var(--ink); }
  .person {
    position: absolute; left: 300px; top: 40px;
    padding-left: 12px; border-left: 1px solid var(--ink);
  }
  .person-name { font-size: 16px; font-weight: 700; color: var(--brand-blue); }
  .person-role { font-size: 12px; color: var(--ink); margin-top: 2px; }
  .contact-list { position: absolute; left: 300px; top: 100px; list-style: none; }
  .contact-item {
    display: flex; align-items: center; gap: 8px;
    font-size: 12.5px; color: var(--ink); height: 23px; white-space: nowrap;
  }
  .contact-icon { width: 16px; height: 16px; flex: none; }
  .front-brand { position: absolute; left: 30px; top: 162px; width: 252px; }
  .front-brand .brand-lockup { gap: 8px; }
  .front-brand .brand-mark { width: 22px; height: 22px; background: var(--brand-blue); }
  .front-brand .brand-name { font-size: 21px; font-weight: 700; color: var(--brand-blue); letter-spacing: .2px; }
  .front-brand .tagline {
    margin-top: 7px; font-size: 7.6px; font-weight: 700; color: var(--ink);
    border-top: 1px solid var(--grey); padding-top: 3px; white-space: nowrap;
  }
  .address-band {
    position: absolute; left: 0; right: 0; top: 250px; height: 40px;
    background: var(--brand-blue);
    display: flex; align-items: center; justify-content: center;
  }
  .address-text { font-size: 14px; color: var(--white); letter-spacing: .1px; white-space: nowrap; }
  .band-end { position: absolute; top: 0; width: 38px; height: 40px; }
  .band-end--left { left: 0; }
  .band-end--right { right: 0; }
</style>
</head>
<body>
<main class="sheet">

  <section class="card card--back" aria-label="Card back">
    <div class="back-brand">
      <div class="brand-lockup">
        <span class="brand-mark"></span>
        <span class="brand-name">GreenHarborPeak</span>
      </div>
      <p class="tagline">Guiding growing firms and teams toward their strongest future</p>
    </div>
    <div class="back-divider"></div>
    <p class="back-web">www.greenharborpeak.com.au</p>
  </section>

  <section class="card card--front" aria-label="Card front">
    <div class="person">
      <p class="person-name">Marcus Hale</p>
      <p class="person-role">Director</p>
    </div>

    <ul class="contact-list">
      <li class="contact-item">
        <svg class="contact-icon" viewBox="0 0 16 16"><circle cx="8" cy="8" r="8" fill="#1b1b1b"/><rect x="5.5" y="3.5" width="5" height="9" rx="1" fill="none" stroke="#fff" stroke-width="1.1"/><circle cx="8" cy="11" r=".6" fill="#fff"/></svg>
        0412 305 778
      </li>
      <li class="contact-item">
        <svg class="contact-icon" viewBox="0 0 16 16"><circle cx="8" cy="8" r="8" fill="#1b1b1b"/><path d="M5 4.5c-.6.6-.6 1.8.6 3.6 1.3 1.9 3 3.3 4.2 3.4.7 0 1.2-.5 1.4-1l-1.6-1.3-.9.7c-.8-.4-1.8-1.5-2.2-2.3l.7-.9L6 5z" fill="#fff"/></svg>
        1300 482 917
      </li>
      <li class="contact-item">
        <svg class="contact-icon" viewBox="0 0 16 16"><circle cx="8" cy="8" r="8" fill="#1b1b1b"/><rect x="4" y="6.5" width="8" height="5" fill="none" stroke="#fff" stroke-width="1"/><rect x="5.5" y="4" width="5" height="2.5" fill="#fff"/></svg>
        1300 482 935
      </li>
      <li class="contact-item">
        <svg class="contact-icon" viewBox="0 0 16 16"><circle cx="8" cy="8" r="8" fill="#1b1b1b"/><rect x="4" y="5" width="8" height="6" fill="none" stroke="#fff" stroke-width="1"/><path d="M4 5l4 3.3L12 5" fill="none" stroke="#fff" stroke-width="1"/></svg>
        sample@greenharborpeak.com.au
      </li>
      <li class="contact-item">
        <svg class="contact-icon" viewBox="0 0 16 16"><circle cx="8" cy="8" r="8" fill="#1b1b1b"/><circle cx="8" cy="8" r="4.2" fill="none" stroke="#fff" stroke-width="1"/><ellipse cx="8" cy="8" rx="1.8" ry="4.2" fill="none" stroke="#fff" stroke-width=".9"/><path d="M3.8 8h8.4" stroke="#fff" stroke-width=".9"/></svg>
        www.greenharborpeak.com.au
      </li>
    </ul>

    <div class="front-brand">
      <div class="brand-lockup">
        <span class="brand-mark"></span>
        <span class="brand-name">GreenHarborPeak</span>
      </div>
      <p class="tagline">Guiding growing firms and teams toward their strongest future</p>
    </div>

    <div class="address-band">
      <svg class="band-end band-end--left" viewBox="0 0 38 40"><path d="M0 0h20l18 20-18 20H0z" fill="#0b2447"/><path d="M22 0l18 20-18 20" fill="none" stroke="#85abd2" stroke-width="1.5"/></svg>
      <p class="address-text">Suite 4 - Level 3/48 Lindqvist Avenue Kellyville Ridge NSW 2763</p>
      <svg class="band-end band-end--right" viewBox="0 0 38 40"><path d="M38 0H18L0 20l18 20h20z" fill="#0b2447"/><path d="M16 0L-2 20l18 20" fill="none" stroke="#85abd2" stroke-width="1.5"/></svg>
    </div>
  </section>

</main>
</body>
</html>
```